Maple Crest Glow Skin Studio needs an 8 page WP redesign

We need a colorful re-design for an 8 page Wordpress website. The current preliminary website is live. The home page URL is http://maplecrestglowskinstudio.example The new logo is live on the website also. I would like a (re)design using the colors that are represented by the new logo file, and any additional complimentary colors. The information regarding the business can be found on the website already, so please review it for insight. The name of the business is "Maple Crest Glow Skin Studio".

Target Market(s)

The targeted website viewer is an adult female between the ages of 30 and 75 who is interested in facial renewal, wart removal and scar removal. This website should inspire in the target viewer the benefits of laser facial renewal, wart removal and new scar removal. Potential website viewers are wanting and searching for improved skin health and appearance. The website must represent the essence of a professional spa business.

Industry/Entity Type

Business

Font styles to use
Sans Serif

Requirements
Must have
• - The phone number placed in a visible and high value widget area that allows mobile phone browser dialing.

```html
<!DOCTYPE html>
<html lang="en">
<head>
<meta charset="utf-8">
<title>Maple Crest Glow Skin Studio</title>
<link href="https://fonts.googleapis.com/css2?family=Open+Sans:wght@300;400;600;700&family=Pinyon+Script&display=swap" rel="stylesheet">
<style>
:root{
  --plum:#3d2338;
  --plum-dark:#2e1a2b;
  --magenta:#a02a9b;
  --magenta-light:#c040bb;
  --lilac:#e9e0ea;
  --lilac-soft:#f3eef3;
  --mauve:#9a8898;
  --ink:#333;
  --heading:#4a2645;
  --line:#e2dce2;
  --white:#fff;
}
*{box-sizing:border-box;margin:0;padding:0}
html,body{width:751px;height:1200px;overflow:hidden}
body{position:relative;background:var(--white);font-family:"Open Sans",Arial,sans-serif;color:var(--ink);font-size:7px;line-height:1.45}
.abs{position:absolute}
a{color:inherit;text-decoration:none}

/* header */
.site-header{left:0;top:0;width:751px;height:72px;background:linear-gradient(#efe8f0,#e3d9e4);border-top:3px solid var(--plum)}
.brand{left:52px;top:18px;display:flex;align-items:center;gap:6px;width:150px}
.brand-dot{width:12px;height:12px;border-radius:50%;background:var(--magenta);flex:none}
.brand-name{font-size:11px;font-weight:600;color:var(--heading);line-height:1.15}
.phone{left:500px;top:8px;display:flex;align-items:center;gap:5px;color:var(--magenta);font-size:11.5px;font-weight:600}
.main-nav{left:262px;top:34px;display:flex}
.main-nav a{font-size:8px;color:#444;padding:6px 9px}
.main-nav a.current{background:#f6f3f6;border:1px solid #ddd}

/* hero */
.hero{left:0;top:72px;width:751px;height:384px}
.hero-bg{width:100%;height:100%;
  background:
    radial-gradient(ellipse 95px 120px at 710px 300px,rgba(178,40,62,.75),rgba(178,40,62,0)),
    radial-gradient(ellipse 150px 190px at 555px 130px,rgba(222,178,160,.95),rgba(222,178,160,0)),
    radial-gradient(ellipse 130px 150px at 480px 60px,rgba(150,105,90,.55),rgba(150,105,90,0)),
    linear-gradient(90deg,#ede7ee 0%,#e2d8e3 40%,#dccbd2 60%,#dcc4c2 100%)}
.hero-title{left:124px;top:162px;font-family:"Pinyon Script",cursive;font-size:33px;color:#2b2128}
.hero-text{left:125px;top:205px;width:255px;font-size:9.6px;line-height:1.35;color:#3a3237}
.hero-btn{left:265px;top:241px;width:106px;height:27px;background:#f7f4f7;border:1px solid #ddd;color:var(--magenta);font-size:12px;text-align:center;line-height:25px}
.hero-arrow{top:298px;width:28px;height:28px;border:1.5px solid rgba(255,255,255,.85);border-radius:50%}

/* service cards */
.card{top:416px;width:218px}
.card-img{width:218px;height:102px;border:3px solid #fff;box-shadow:0 0 0 1px #ddd}
.card h3{font-weight:400;font-size:13.5px;color:var(--heading);margin:8px 0 5px 5px}
.card p{font-size:6.6px;margin-left:5px;line-height:1.35}
.card .more{font-style:italic;color:var(--magenta);margin:6px 0 0 5px;display:block;font-size:7px}

/* main */
.section-title{font-weight:400;font-size:14px;color:var(--heading)}
.copy p{font-size:7px;text-align:justify;margin-bottom:10px;line-height:1.5}
.photo{border:3px solid #fff;box-shadow:0 0 0 1px #ddd}
.read-more{left:416px;top:1061px;width:58px;height:22px;background:var(--magenta);color:#fff;font-size:7.5px;text-align:center;line-height:22px;border-radius:2px}
.share{top:1062px;display:flex;gap:6px;left:48px}
.share-item{width:26px}
.share-count{height:16px;border:1px solid #ccc;background:#fff;font-size:7px;text-align:center;line-height:14px;color:#777}
.share-btn{height:10px;margin-top:3px;background:#eee;border:1px solid #ccc}

/* sidebar */
.search{left:492px;top:598px;width:214px;height:28px;border:1px solid #ddd;background:#f4f4f4;padding:7px 12px;font-size:7.5px;color:#666}
.widget{left:492px;width:214px;border:1px solid #e3e3e3;background:#fff;overflow:hidden}
.widget h4{font-weight:400;font-size:14px;color:#fff;padding:5px 11px;margin:2px 2px 4px}
.widget li{list-style:none;font-size:7.5px;padding:6px 6px 6px 18px;border-bottom:1px solid #eee;position:relative;line-height:1.3}
.widget li::before{content:"";position:absolute;left:8px;top:9px;border:3px solid transparent;border-left:3px solid #666}
.posts h4{background:linear-gradient(var(--plum),var(--plum-dark))}
.archives h4{background:linear-gradient(var(--magenta-light),var(--magenta))}
.meta h4{background:var(--mauve)}
.roomy li{padding:8px 6px 8px 18px}
.roomy li::before{top:11px}

/* footer */
.site-footer{left:0;top:1108px;width:751px;height:92px;background:linear-gradient(var(--plum),#4d2c49)}
.foot-nav{left:0;width:751px;top:20px;display:flex;justify-content:center;gap:21px;color:#e9dde8;font-size:8px}
.foot-social{left:0;width:751px;top:45px;display:flex;justify-content:center;gap:7px}
.foot-social span{width:17px;height:17px;border-radius:50%;background:#3f8fd0}
.copyright{left:0;width:751px;top:76px;text-align:center;color:#d8cbd6;font-size:6.8px}
</style>
</head>
<body>

<header class="abs site-header">
  <div class="abs brand"><span class="brand-dot"></span><span class="brand-name">Maple Crest Glow Skin Studio</span></div>
  <a class="abs phone" href="tel:18005550142">
    <svg width="11" height="11" viewBox="0 0 24 24"><path fill="#a02a9b" d="M6.6 10.8a15 15 0 0 0 6.6 6.6l2.2-2.2c.3-.3.7-.4 1-.2 1.1.4 2.3.6 3.6.6.6 0 1 .4 1 1V20c0 .6-.4 1-1 1C10.6 21 3 13.4 3 4c0-.6.4-1 1-1h3.5c.6 0 1 .4 1 1 0 1.3.2 2.5.6 3.6.1.3 0 .7-.2 1z"/></svg>
    Call Us : 1-800 . 555 . 0142
  </a>
  <nav class="abs main-nav">
    <a class="current">Home</a><a>About Us</a><a>Skin Renewal</a><a>Scar Removal</a><a>Your Visit</a><a>Contact Us</a><a>Blog</a>
  </nav>
</header>

<section class="abs hero">
  <div class="hero-bg" role="img" aria-label="Smiling woman holding red daisies beside soft faded dandelion flowers"></div>
  <h1 class="abs hero-title">Lorium Ipsum</h1>
  <p class="abs hero-text">Morbi ac lacus sit amet nisl dignissim condimentum sit amet sit amet nibh. Ut eget pulvinar nisl, sed maximus enim.</p>
  <a class="abs hero-btn">Get Started</a>
  <svg class="abs hero-arrow" style="left:54px" viewBox="0 0 28 28"><path d="M16 8l-6 6 6 6" fill="none" stroke="#fff" stroke-width="1.5"/></svg>
  <svg class="abs hero-arrow" style="left:89px" viewBox="0 0 28 28"><path d="M12 8l6 6-6 6" fill="none" stroke="#fff" stroke-width="1.5"/></svg>
</section>

<article class="abs card" style="left:42px">
  <div class="card-img" style="background:linear-gradient(90deg,#f7f6f6,#e6d3c6)" role="img" aria-label="Woman touching her smooth cheek"></div>
  <h3>Laser Skin Therapy</h3>
  <p>Morbi ac lacus sit amet nisl dignissim condimentum sit amet sit amet nibh. Ut eget pulvinar nisl, sed maximus enim.</p>
  <a class="more">Readmore</a>
</article>
<article class="abs card" style="left:267px">
  <div class="card-img" style="background:linear-gradient(90deg,#dfe8ee,#ead9cf)" role="img" aria-label="Woman's face with treatment point markers"></div>
  <h3>Scar Removal</h3>
  <p>Morbi ac lacus sit amet nisl dignissim condimentum sit amet sit amet nibh. Ut eget pulvinar nisl, sed maximus enim.</p>
  <a class="more">Readmore</a>
</article>
<article class="abs card" style="left:491px">
  <div class="card-img" style="background:linear-gradient(90deg,#eee5df,#dcc5b6,#eee5df)" role="img" aria-label="Before and after portrait of clearer skin"></div>
  <h3>Wart Removal</h3>
  <p>Morbi ac lacus sit amet nisl dignissim condimentum sit amet sit amet nibh. Ut eget pulvinar nisl, sed maximus enim.</p>
  <a class="more">Readmore</a>
</article>

<main>
  <h2 class="abs section-title" style="left:49px;top:603px">Welcome To Have you considered Laser Skin Renewal Therapy?</h2>
  <div class="abs copy" style="left:49px;top:634px;width:282px">
    <p>You will truly love laser skin renewal if your skin is showing signs of premature aging or the skin has sustained sun damage. Conditions such as excessive redness due to sun exposure or fine lines will be concerns of the past. In fact, laser skin therapy is a unique and innovative way to enjoy youthful and healthy skin without resorting to painful and inconvenient surgery. Both men and women are receiving benefits from laser skin therapy.</p>
    <p>The literature contains ample scientific evidence to support laser skin renewal. After this therapy, your skin will produce collagen, which reduces and minimizes the appearance of fine lines and wrinkles. Imagine getting all this with minimal pain and no downtime? Doesn't it make you feel like getting in touch with our laser skin specialist today?</p>
  </div>
  <div class="abs photo" style="left:340px;top:633px;width:117px;height:142px;background:linear-gradient(#d9c3b8,#f0e6e1)" role="img" aria-label="Woman relaxing during a facial treatment"></div>

  <h2 class="abs section-title" style="left:44px;top:795px">Laser Skin Renewal is Innovative and Unique</h2>
  <div class="abs photo" style="left:46px;top:827px;width:119px;height:221px;background:linear-gradient(#eef0ee,#c9cfcd)" role="img" aria-label="Laser skin treatment machine"></div>
  <div class="abs copy" style="left:197px;top:825px;width:282px">
    <p>Laser skin therapy is a non-invasive procedure that is extremely safe and effective. Above all, it is discrete and you never have to worry about family, friends and acquaintances, finding out that you have had treatment for fine lines and wrinkles.</p>
    <p>After each treatment, you will notice subtle but definite results. You will never have to hide indoors to wait for the skin irritation or bruising to disappear. The treatment sessions are comfortable and there is no worry about using topical anesthetic gels.</p>
    <p style="text-align:right;margin-right:5px">Seeing is Believing</p>
    <p><b>Laser skin renewal</b> does produce outstanding results. After mere five treatment sessions, you will notice a youthful glow about your skin and you also will find your skin looking smooth with an even tone.</p>
    <p>People, who have undergone laser treatment, also find their complexion is healthier and creamier in appearance. Furthermore, you will find the size of large pore reduced to a significant extent and even minor imperfections on your face will not be as noticeable.</p>
    <p>While you may notice subtle changes and results after a single treatment, when you combine the results of multiple treatments, the results can be dramatic and startling.</p>
  </div>

  <div class="abs share">
    <div class="share-item"><div class="share-count">0</div><div class="share-btn"></div></div>
    <div class="share-item"><div class="share-count">0</div><div class="share-btn"></div></div>
    <div class="share-item" style="width:34px"><div class="share-count">0</div><div class="share-btn"></div></div>
    <div class="share-item"><div class="share-count"></div><div class="share-btn"></div></div>
    <div class="share-item"><div class="share-count" style="border-radius:3px"></div><div class="share-btn"></div></div>
    <div class="share-item"><div class="share-count">0</div><div class="share-btn"></div></div>
  </div>
  <a class="abs read-more">Read more</a>
</main>

<aside>
  <div class="abs search">Search
    <svg style="position:absolute;right:12px;top:8px" width="11" height="11" viewBox="0 0 12 12"><circle cx="5" cy="5" r="3.8" fill="none" stroke="#777" stroke-width="1.4"/><path d="M8 8l3 3" stroke="#777" stroke-width="1.6"/></svg>
  </div>
  <section class="abs widget posts" style="top:630px;height:136px">
    <h4>Recent Posts</h4>
    <ul>
      <li>The Benefits of Laser Skin Rejuvenation</li>
      <li>Duis sit amet rutrum nisl, sed ullamcorper augue. Nulla felis velit, tempus eget fermentum bibendum, varius vel justo.</li>
      <li style="border:none">Vestibulum mauris velit, tincidunt quis libero vel, rutrum pellentesque turpis. Proin ac urna facilisis</li>
    </ul>
  </section>
  <section class="abs widget archives roomy" style="top:771px;height:172px">
    <h4>Archives</h4>
    <ul><li>December 2014</li><li>November 2014</li><li>October 2014</li><li>September 2014</li><li style="border:none">August 2014</li></ul>
  </section>
  <section class="abs widget meta roomy" style="top:945px;height:146px">
    <h4>Meta</h4>
    <ul><li>Log in</li><li>Entries RSS</li><li>Comments RSS</li><li style="border:none">Publisher.example</li></ul>
  </section>
</aside>

<footer class="abs site-footer">
  <nav class="abs foot-nav"><a>Home</a><a>About Us</a><a>Skin Renewal</a><a>Scar Removal</a><a>Your Visit</a><a>Contact Us</a><a>Blog</a></nav>
  <div class="abs foot-social"><span></span><span></span><span></span><span></span></div>
  <p class="abs copyright">© 2014 www.maplecrestglowskinstudio.example</p>
</footer>

</body>
</html>
```